Flyer-Design für Tauchunternehmen im südlichen Ägypten
Zielgruppe
Wir sind ein Tauchunternehmen im südlichen Ägypten, mit dem Hauptaugenmerk auf unser Tauchcenter und Sataya.
Aufgabenstellung
Es ist mir bewusst, dass es viel Content ist. Dieser kann ggf. auch angepasst werden. Der Flyer sollte in einem gängigen Format gedruckt werden können. Lieber mehrseitig, all flächenmässig zu gross.
Die beiden erwähnten Boote gehören unbedingt zu Sataya.
Die Zip Dateien sind auf die Themen abgestimmt, resp. das allgemeine Diving kann beliebig eingesetzt werden. Je ein Exemplar in Deutsch und Englisch wäre super. Beide Texte liegen vor.
Velmora Diving Safari - Entdecke das Rote Meer
Wir zeigen euch unser tolles, vielfältiges zu Hause mit den schönsten Tauchplätzen.
Ob ihr erfahrene Taucher seid oder gerade erst euer Tauchabenteuer begonnen habt, erlebt mit uns die Schönheit der Unterwasserwelt mit ihren vielfältigen Korallen und Fischen.
Entfliehe mit uns dem Alltag.
Wir freuen uns, dich bei uns begrüssen zu dürfen!
Team Velmora Diving Safari
Omar & Carla
…..and into the ocean we go, to lose our mind and find our soul
Velmora Diving Safari - Discover the Red Sea
We show you our great, diverse home with the most beautiful dive sites.
Whether you are an experienced diver or just starting your diving adventure, discover with us the beauty of the underwater world with its varied corals and fish.
Escape the daily routine with us.
We look forward to welcoming you!
.....and into the ocean we go, to lose our mind and find our soul
Tauchcenter
Wir sind im Hotel Brevanto, südlich von El Quseir zu Hause. Von hier aus starten wir täglich zum Tauchen und Schnorcheln am Hausriff, vom Strand an die umliegenden Riffe und unseren Tagesbooten ab Port Ghalib und Hamata. Unser Team begleitet dich professionell bei deinen ersten Atemzügen unter Wasser, bildet dich nach DQX und VORK-Standard aus oder führt dich sicher entlang der Tauchplätze.
Wir offerieren attraktive Arrangements mit Hotel und Tauchen..

```html
<!DOCTYPE html>
<html lang="en">
<head>
<meta charset="utf-8">
<title>Velmora Diving Safari – Flyer</title>
<link href="https://fonts.googleapis.com/css2?family=Anton&family=Arimo:wght@700&family=Ubuntu:wght@400;500&display=swap" rel="stylesheet">
<style>
  :root {
    --page: #d6d6d7;
    --panel: #0d5aa7;
    --panel-deep: #0a4b93;
    --yellow: #f7e61a;
    --white: #ffffff;
    --sea-light: #2b8fd6;
    --sea-mid: #1663b0;
    --sea-dark: #0a3c7c;
  }
  * { box-sizing: border-box; margin: 0; padding: 0; }
  html, body { width: 1200px; height: 1200px; overflow: hidden; }
  body {
    background: var(--page);
    font-family: "Ubuntu", sans-serif;
    color: var(--white);
    position: relative;
  }
  .spread {
    position: absolute;
    left: 215px;
    width: 770px;
    height: 544px;
    display: flex;
  }
  .spread--outside { top: 39px; background: var(--panel); }
  .spread--inside { top: 617px; }
  .spread__backdrop {
    position: absolute; inset: 0;
    background: radial-gradient(ellipse at 45% 40%, #2a7cc6 0%, #1560ae 45%, #0b4e98 100%);
  }
  .panel { position: relative; width: 256.67px; height: 100%; }
  .photo { position: absolute; }
  .photo--framed { border: 2px solid var(--yellow); }
  .copy {
    position: absolute;
    font-size: 10.6px;
    line-height: 16.3px;
  }
  .heading {
    position: absolute;
    font-family: "Arimo", sans-serif;
    font-weight: 700;
    color: var(--yellow);
    font-size: 16.5px;
  }
  /* outside spread */
  .contacts__title {
    position: absolute; top: 196px; left: 0; width: 100%;
    text-align: center;
    font-family: "Arimo", sans-serif; font-weight: 700;
    color: var(--yellow); font-size: 21px;
  }
  .contacts__list {
    position: absolute; top: 232px; left: 10px;
    list-style: none;
    font-size: 16.4px; line-height: 28.7px;
    white-space: nowrap;
  }
  .cover__title {
    position: absolute; top: 56px; left: 11px;
    font-family: "Anton", sans-serif;
    color: var(--yellow);
    font-size: 24.5px; line-height: 31px;
    letter-spacing: 0.2px;
  }
  .cover__brand {
    position: absolute; top: 11px; right: 8px;
    display: flex; align-items: center; gap: 4px;
    font-size: 8px; color: var(--white);
  }
  .cover__brand-dot {
    width: 10px; height: 10px; border-radius: 50%;
    background: var(--white);
  }
  .cover__copy {
    position: absolute; top: 184px; left: 16px; right: 8px;
    font-size: 12.8px; line-height: 17px;
  }
  .cover__copy p + p { margin-top: 17px; }
  .inside-copy { font-size: 10.8px; line-height: 17px; }
  .inside-copy--tight { line-height: 15.8px; }
</style>
</head>
<body>

<!-- Outside spread -->
<section class="spread spread--outside">
  <div class="panel panel--boat">
    <div class="photo photo--framed" style="left:15px;top:14px;width:226px;height:118px;background:linear-gradient(180deg,#cfe3f4 0%,#8fb8dd 45%,#1d3f72 70%,#234c82 100%);" role="img" aria-label="Motor yacht Sahira cruising at speed on open sea"></div>
    <p class="copy" style="top:139px;left:15px;width:232px;">MY Sahira was built in 2019. With a length of 30 metres and a beam of 8 metres, the steel-constructed boat comfortably accommodates 18 guests.<br>5 twin bed cabins and 2 double bed cabins are located on the lower deck and 2 single bed cabins on the upper deck.</p>
    <div class="photo photo--framed" style="left:15px;top:261px;width:226px;height:117px;background:linear-gradient(180deg,#d8c48a 0%,#9a7a45 35%,#3a8fb0 55%,#7a5a35 80%,#2c3f58 100%);" role="img" aria-label="Yacht restaurant lounge with sofas and buffet"></div>
    <p class="copy" style="top:385px;left:15px;width:232px;">The restaurant on the main deck serves 3 buffets a day, and the spacious dive deck is where you get ready for adventure.<br>On the top deck, there is plenty of shaded seating and a bar for socialising and relaxing.<br>On the top deck, comfortable loungers await, ideal for enjoying the sun or watching the stars.</p>
  </div>

  <div class="panel panel--contacts">
    <div class="photo" style="left:0;top:0;width:100%;height:175px;background:radial-gradient(circle at 55% 45%,#f1a13a 0%,#d9822a 18%,#2f7cc4 45%,#0f5aa8 100%);" role="img" aria-label="School of orange anthias fish in blue water"></div>
    <h2 class="contacts__title">CONTACTS</h2>
    <ul class="contacts__list">
      <li>Omar +20 100 555 0142</li>
      <li>Carla +41 79 555 01 23</li>
      <li>www.velmoradivingsafari.com</li>
      <li>info@velmoradivingsafari.com</li>
      <li>Friendbook: velmoradiving.20</li>
      <li>Snapgram: velmora_diving_safari</li>
      <li>ViewTube: Velmora Diving Safari</li>
    </ul>
    <div class="photo" style="left:0;top:449px;width:100%;height:95px;background:linear-gradient(180deg,#1a4f86 0%,#6f8fa8 45%,#c3cfd6 60%,#2f5f8e 100%);" role="img" aria-label="Hard coral reef with a fish swimming over it"></div>
  </div>

  <div class="panel panel--cover">
    <div class="photo" style="left:0;top:0;width:100%;height:175px;background:linear-gradient(180deg,#3a96dc 0%,#1b6cbf 50%,#0f4f9c 100%);" role="img" aria-label="Oceanic whitetip shark swimming in deep blue water"></div>
    <div class="cover__brand"><span>Velmora Diving Safari</span><span class="cover__brand-dot"></span></div>
    <h1 class="cover__title">Velmora Diving Safari -<br>Discover the Red Sea</h1>
    <div class="cover__copy">
      <p>We show you our great, diverse home with the most beautiful dive sites. Whether you are an experienced diver or just starting your diving adventure, discover with us the beauty of the underwater world with its varied corals and fish.<br>Escape the daily routine with us.</p>
      <p>We look forward to welcoming you!</p>
      <p>Team Velmora Diving Safari<br>Omar &amp; Carla<br>.....and into the ocean we go, to lose our mind and find our soul.</p>
    </div>
    <div class="photo" style="left:0;top:449px;width:100%;height:95px;background:linear-gradient(180deg,#2a3f8c 0%,#243a84 60%,#1e3276 100%);" role="img" aria-label="Hammerhead shark in dark blue water"></div>
  </div>
</section>

<!-- Inside spread -->
<section class="spread spread--inside">
  <div class="spread__backdrop" role="img" aria-label="Faint underwater background with a spotted ray"></div>

  <div class="panel panel--centre">
    <div class="photo photo--framed" style="left:15px;top:12px;width:226px;height:163px;background:linear-gradient(180deg,#4aa2d8 0%,#1c6aa8 40%,#0e3f6e 75%,#0a2f55 100%);" role="img" aria-label="Two scuba divers underwater above a reef"></div>
    <h2 class="heading" style="top:192px;left:15px;">Diving Centre</h2>
    <p class="copy inside-copy" style="top:218px;left:15px;width:232px;">We are based at the Hotel Brevanto, south of El Quseir. From here we depart daily for diving and snorkeling along the house reef, from the beach to the surrounding reefs and our daily boats from Port Ghalib and Hamata. Our team will accompany you professionally during your first breaths under water, train you according to DQX and VORK standards or guide you safely along the dive sites.We offer attractive packages with hotel and diving.</p>
    <h2 class="heading" style="top:424px;left:15px;">Daily boat</h2>
    <p class="copy inside-copy" style="top:450px;left:15px;width:232px;">Enjoy a day at sea, diving and snorkeling in Marsa Mubarak. If you're lucky, you'll see the dugong and the big turtles. Snorkel in Sataya with the dolphins and along the islands of Hamata.</p>
  </div>

  <div class="panel panel--trips">
    <h2 class="heading" style="top:12px;left:20px;">Liveaboards</h2>
    <p class="copy inside-copy" style="top:38px;left:20px;width:232px;">Experience a fantastic week on the Red Sea and explore some of the most stunning and colourful dive sites in the world.<br>Find your favourite sites on our North Tour, South Tour or Deep South.</p>
    <h2 class="heading" style="top:144px;left:24px;">Full charter</h2>
    <p class="copy inside-copy" style="top:168px;left:24px;width:224px;">Are you a larger group of divers or a dive club and want to be among yourselves on the boat? Then a full charter may be the best option.</p>
    <p class="copy" style="top:244px;left:24px;width:224px;font-size:10.8px;line-height:18.8px;">Let us know your ideas, conditions, wishes and diving experience. We will plan an individual full charter considering your details and the conditions at hand.</p>
    <div class="photo photo--framed" style="left:16px;top:340px;width:225px;height:187px;background:linear-gradient(180deg,#1c4f8a 0%,#2a5f98 30%,#d8dde2 60%,#3a4a5c 80%,#1d4e86 100%);" role="img" aria-label="Group of divers on an inflatable boat at sea"></div>
  </div>

  <div class="panel panel--boats">
    <div class="photo photo--framed" style="left:14px;top:14px;width:226px;height:104px;background:linear-gradient(180deg,#d9e6ef 0%,#bcd0de 40%,#2a6c8e 60%,#c8b48c 85%,#b9a27a 100%);" role="img" aria-label="Dive centre building on the beach"></div>
    <h2 class="heading" style="top:129px;left:19px;">Diving courses</h2>
    <p class="copy inside-copy inside-copy--tight" style="top:155px;left:20px;width:236px;">Learn to dive with our passionate instructors. As a partner of VORK and DQX we train you in all levels from Scuba Diver to Dive Master. The courses can also be done during a liveaboard, depending on the conditions.</p>
    <h2 class="heading" style="top:244px;left:19px;">Boats</h2>
    <p class="copy inside-copy" style="top:270px;left:19px;width:200px;font-size:10.8px;line-height:14.6px;">Our boats, Sahira and Coralis 1, fully adapted to the needs of divers and snorkelers.</p>
    <div class="photo photo--framed" style="left:14px;top:320px;width:226px;height:103px;background:linear-gradient(180deg,#e6eef5 0%,#c9d9e8 40%,#f4f6f8 60%,#5d8fb8 80%,#3f78a8 100%);" role="img" aria-label="White motor yacht Coralis 1 at anchor"></div>
    <p class="copy inside-copy" style="top:433px;left:19px;width:236px;font-size:10.8px;line-height:16.4px;">MY Coralis 1 was built in 2021. With a length of 32 metres and a beam of 8 metres, the steel-constructed boat comfortably ccommodates 24 guests.<br>8 cabins with twin beds are located on the lower deck and 4 cabins on the upper deck.</p>
  </div>
</section>

</body>
</html>
```